Unique & Creative Business Card for Lumavessence

Would you please create a unique design that is soft and appealing to people who seek to raise vibrational energy for themselves, for animals (domestic or wild), or for the environment.

Optional: Elements could include, landscapes, wild animals, feathers, vibrational patterns, the elements (Earth, water, fire, air and space). Images that are calming.

With Thanks!

Target Market(s)

People and businesses who are into the environment, animal welfare, alternative health.

Contact Information for Business Card

Moira Bell
Energist
mb@lumavessence.example
lumavessence.example

Requirements
Must have
• Lumavessence logo (attached)
Symbols that represent our main services: Natural environment, animal, human and energy.
Our strapline ‘Achieving Vibrational Equilibrium’
Nice to have
• Clear and easy to read
Colours based on nature/soft colours

```html
<!DOCTYPE html>
<html lang="en">
<head>
<meta charset="utf-8">
<title>Lumavessence Business Card</title>
<link href="https://fonts.googleapis.com/css2?family=Montserrat:wght@400;500&family=Dancing+Script:wght@700&display=swap" rel="stylesheet">
<style>
  :root {
    --backdrop: #907a98;
    --lilac: #c2b4c8;
    --lilac-soft: #e6dfe9;
    --lilac-pale: #f4f1f6;
    --plum: #8b6a98;
    --brand-blue: #3f6fb5;
    --ink: #5a5a5e;
    --white: #ffffff;
  }
  * { box-sizing: border-box; margin: 0; padding: 0; }
  html, body {
    width: 1200px; height: 783px; overflow: hidden;
    background: var(--backdrop);
    font-family: "Montserrat", sans-serif;
  }
  .stage { position: relative; width: 1200px; height: 783px; }
  .card {
    position: absolute; top: 237px;
    width: 540px; height: 309px;
    overflow: hidden;
    box-shadow: 0 10px 24px rgba(40, 20, 50, 0.35);
  }

  /* Back side */
  .card-back { left: 45px; background: var(--lilac); }
  .vibration-field {
    position: absolute;
    border-radius: 50%;
    background: radial-gradient(ellipse at center,
      rgba(255,255,255,0) 45%,
      rgba(255,255,255,0.28) 58%,
      rgba(255,255,255,0.1) 66%,
      rgba(255,255,255,0) 72%);
  }
  .vibration-field.top-right { right: -150px; top: -170px; width: 420px; height: 420px; }
  .vibration-field.bottom-left { left: -190px; bottom: -220px; width: 520px; height: 440px; }
  .leaf-sprig {
    position: absolute;
    background: radial-gradient(ellipse at center, rgba(139,106,152,0.14), rgba(139,106,152,0) 70%);
  }
  .card-back .leaf-sprig.left { left: 14px; top: 95px; width: 170px; height: 60px; }
  .card-back .leaf-sprig.right { right: 100px; top: 110px; width: 80px; height: 140px; }
  .brand-mark {
    position: absolute; display: flex; align-items: center; gap: 10px;
    color: var(--brand-blue); font-weight: 500; letter-spacing: 0.04em;
  }
  .card-back .brand-mark {
    left: 50%; top: 50%; transform: translate(-50%, -50%);
    font-size: 24px;
  }
  .brand-dot {
    border: 3px solid var(--brand-blue); border-radius: 50%;
    background: var(--lilac-soft);
  }
  .card-back .brand-dot { width: 34px; height: 34px; }

  /* Front side */
  .card-front { left: 615px; background: var(--white); }
  .card-front .leaf-sprig {
    left: -30px; top: -30px; width: 240px; height: 150px;
    background: radial-gradient(ellipse at 40% 45%, var(--lilac-pale) 35%, rgba(244,241,246,0) 72%);
  }
  .card-front .brand-mark { left: 30px; top: 120px; font-size: 16px; }
  .card-front .brand-dot { width: 24px; height: 24px; border-width: 2px; }
  .contact { position: absolute; left: 232px; top: 56px; }
  .person-name {
    font-family: "Dancing Script", cursive;
    font-size: 44px; font-weight: 700; color: var(--plum); line-height: 1;
  }
  .person-role {
    display: inline-block; margin-top: 6px;
    font-size: 12px; font-weight: 500; letter-spacing: 0.28em;
    color: var(--plum);
    padding-bottom: 4px; border-bottom: 2px solid var(--plum);
  }
  .contact-list { list-style: none; margin-top: 12px; }
  .contact-list li {
    display: flex; align-items: center; gap: 9px;
    font-size: 15px; line-height: 1.6;
  }
  .contact-text { color: var(--ink); }
  .contact-list svg { width: 14px; height: 14px; flex: none; }
  .strap-band {
    position: absolute; left: 0; right: 0; top: 236px; height: 28px;
    background: var(--lilac);
    display: flex; align-items: center; justify-content: center; gap: 12px;
    color: var(--white); font-size: 12px; letter-spacing: 0.55em;
  }
  .strap-band .rule { width: 22px; height: 2px; background: var(--white); }
</style>
</head>
<body>
<main class="stage">

  <section class="card card-back" aria-label="Card back">
    <div class="vibration-field top-right" role="img" aria-label="Dotted vibrational wave pattern"></div>
    <div class="vibration-field bottom-left" role="img" aria-label="Dotted vibrational wave pattern"></div>
    <div class="leaf-sprig left" role="img" aria-label="Line-drawn leaf sprig"></div>
    <div class="leaf-sprig right" role="img" aria-label="Line-drawn leaf sprig"></div>
    <div class="brand-mark">
      <span class="brand-dot"></span>
      <span class="brand-name">Lumavessence</span>
    </div>
  </section>

  <section class="card card-front" aria-label="Card front">
    <div class="leaf-sprig" role="img" aria-label="Line-drawn leaf sprigs on a soft lilac wash"></div>
    <div class="brand-mark">
      <span class="brand-dot"></span>
      <span class="brand-name">Lumavessence</span>
    </div>
    <div class="contact">
      <h1 class="person-name">Moira Bell</h1>
      <p class="person-role">ENERGIST</p>
      <ul class="contact-list">
        <li>
          <svg viewBox="0 0 16 16" aria-hidden="true"><rect x="1" y="3" width="14" height="10" fill="#5a5a5e"/><path d="M1 3l7 6 7-6" fill="none" stroke="#fff" stroke-width="1.4"/></svg>
          <span class="contact-text">mb@lumavessence.example</span>
        </li>
        <li>
          <svg viewBox="0 0 16 16" aria-hidden="true" fill="none" stroke="#5a5a5e" stroke-width="1.2"><circle cx="8" cy="8" r="6.5"/><ellipse cx="8" cy="8" rx="3" ry="6.5"/><path d="M1.5 8h13M2.5 4.8h11M2.5 11.2h11"/></svg>
          <span class="contact-text">lumavessence.example</span>
        </li>
      </ul>
    </div>
    <div class="strap-band">
      <span class="rule"></span>
      <span class="strap-text">LUMAVESSENCE</span>
      <span class="rule"></span>
    </div>
  </section>

</main>
</body>
</html>
```